PLUM- company with a mission

PLUM LLC stands for pure living under moonlight (non profit arm is called bright lantern foundation)—our business is based out of New York City and has a non-profit arm where for every bar you purchase, we donate a bar (don’t want any designs that limits us to only soap). Currently working with South Africa. We want the focus to be organic/natural soap with a mission.
What our website needs to…achieve:
Purpose = branding, building up interesting leaving up to launch date, then a full functional site for selling soap (for now) with a mission. With that said, there will need to be a page designed for “COMING SOON” – with a place to post our teaser 30 second video (kind of like a commercial/movie trailer) – until everything else is done.
We are the first in the industry to do one for one (or …50/50). Most companies that do charity work are mostly for every $$$ we donate $0.10, or 1% of XXX. We are starting out to run the non-profit arm as well not just after we reach certain milestones. In addition, we will be transparent for the non-profit side whereas most of the time when you donate, you have no idea where the money ends up going.
IN ADDITION: we still need to be clean/elegant – and selling our soap; so website will need to 1. Showcase our products, 2. Be very clear that we have a mission (not sure if there is a way to show case both our soap AND our mission)
Some sites we like:
Velbrook.com—like them in terms of business model—in terms of their website: like how their site is clean and friendly, but it seems too cluttered
www.quindelmarsh.com -- similar business model, www.pemaroux.com, kelvashop.com, ridgelybar.com
Duvik.com: like this a lot better than fernwicke.com, however, major dislike of the typeface. Okay about the neutral colors…although feel like we need something a bit more cheerful here and there for our mission
Zlabel.net, kelvashop.com, castlewren.com: like how they are clean and showcase well
**** However, our site also needs to convey messages like: www.feverfreeworld.org, www.cleanhandsunited.org
Looking for a clean, simple design. Modern, clutter-free, and inviting. Definitely do not want an arts and crafty/flowery feel. We do need something…cheerful for our nonprofit purposes.
Examples of sites we don’t like: marigoldhaus.com, petalpressbar.com
7 pages/ tabs maybe? (About us…video page (to show case what we are doing –currently my partner is in South Africa filming what our mission will be able to do – give children and those in need soap), FAQs, soap products, terms & conditions, contact us page, blog page……nothing too crazy).
For now, for designing purposes, please use any example texts whether it’s the about us page, mission page..policies.. and for the soap/products pages—please use example you can find online – it is fine, we just need the design done for now.
I have also attached our logo file. Please let me know if you have any questions! Thanks!
Something to consider....
velbrook.com and quindelmarsh.com are probably our largest competitor out of all the websites I mentioned as they have a very similar business model where it is is a company with a mission. Homepage makes that clear that for every pair of shoes/ glasses you purchase, they give a pair. Another thing to note...is that they have been in business for a few years so their website probably have changed to more commercial than focusing/marketing on the mission of doing good. While we don't want that to be the total focus, we do need it to be present on the homepage/front page.
Non-Profit

```html
<!DOCTYPE html>
<html lang="en">
<head>
<meta charset="utf-8">
<title>PLUM – About Us</title>
<link href="https://fonts.googleapis.com/css2?family=Arimo:wght@400;700&family=Inter:wght@200&family=Roboto:wght@400;700&display=swap" rel="stylesheet">
<style>
  :root {
    --orange: #f4a460;
    --orange-deep: #f39a4f;
    --ink: #333333;
    --text: #6f6f6f;
    --muted: #8a8a8a;
    --line: #e2e2e2;
    --frame: #d4d4d4;
    --footer: #333333;
    --white: #ffffff;
  }
  * { box-sizing: border-box; margin: 0; padding: 0; }
  html, body { width: 1200px; height: 900px; overflow: hidden; background: var(--white); }
  body { position: relative; font-family: "Arimo", Arial, sans-serif; color: var(--text); }

  .hero {
    position: absolute; left: 0; top: 0; width: 1200px; height: 277px;
    background: linear-gradient(90deg, #a9a9a9 0%, #cfcfcf 25%, #e4e2e0 50%, #f2f1f0 75%, #e8e8e8 100%);
  }
  .topbar {
    position: absolute; left: 0; top: 0; width: 1200px; height: 27px;
    background: rgba(255,255,255,0.75);
    font-size: 9px; letter-spacing: 0.5px; color: #444;
  }
  .topbar .account { position: absolute; left: 50px; top: 9px; }
  .topbar .account span { margin: 0 8px; }
  .topbar .contact { position: absolute; right: 50px; top: 9px; color: #111; }
  .topbar .contact span { margin: 0 12px; }
  .topbar svg { vertical-align: -2px; }

  .navband { position: absolute; left: 0; top: 71px; width: 1200px; height: 55px; background: var(--white); }
  .nav { position: absolute; right: 49px; top: 71px; height: 55px; display: flex; border-left: 1px solid var(--line); }
  .nav a {
    display: flex; align-items: center; padding: 0 14px; height: 55px;
    font-size: 12.5px; color: #555; text-decoration: none; border-right: 1px solid var(--line);
  }
  .nav a.active { border-top: 2px solid var(--orange); padding-bottom: 2px; }
  .nav a.search { width: 51px; justify-content: center; }

  .brand { position: absolute; left: 50px; top: 76px; display: flex; align-items: center; gap: 10px; }
  .brand .mark { width: 44px; height: 44px; border-radius: 50%; background: var(--orange); }
  .brand .name { font-size: 30px; font-weight: 700; color: var(--orange); letter-spacing: 1px; }

  .hero-photo {
    position: absolute; left: 200px; top: 126px; width: 1000px; height: 151px;
    background: linear-gradient(90deg, rgba(220,200,190,0.0) 0%, rgba(240,225,215,0.35) 10%, rgba(255,255,255,0.0) 40%, rgba(250,250,250,0.5) 80%);
  }
  .page-title {
    position: absolute; left: 0; width: 1250px; top: 170px; text-align: center;
    font-family: "Inter", Arial, sans-serif; font-weight: 200; font-size: 58px; letter-spacing: -1px;
    color: var(--white); text-shadow: 0 1px 3px rgba(0,0,0,0.35);
  }
  .back-home { position: absolute; right: 49px; top: 245px; display: flex; align-items: center; gap: 8px; font-size: 12px; color: #b3b3b3; }
  .back-home .arrow-box { width: 24px; height: 24px; border: 1px solid #9a9a9a; background: rgba(255,255,255,0.6); display: flex; align-items: center; justify-content: center; }

  .categories { position: absolute; left: 51px; top: 296px; width: 273px; height: 209px; border: 2px solid var(--frame); padding: 17px 20px 0 18px; }
  .categories h3 { font-size: 14px; font-weight: 700; color: var(--ink); padding-bottom: 15px; border-bottom: 1px solid var(--line); }
  .categories ul { list-style: none; }
  .categories li { font-size: 11px; color: #666; letter-spacing: 0.3px; height: 29.6px; line-height: 30px; border-bottom: 1px solid var(--line); padding-left: 14px; position: relative; }
  .categories li:last-child { border-bottom: none; }
  .categories li::before { content: ""; position: absolute; left: 0; top: 13px; width: 4px; height: 4px; border: 1px solid #bbb; border-radius: 50%; }

  .media { position: absolute; left: 51px; width: 273px; height: 158px; }
  .media.video { top: 517px; background: linear-gradient(135deg, #7aa65a 0%, #5a4030 40%, #3b2a22 70%, #8a6a50 100%); }
  .media.video .play { position: absolute; left: 110px; top: 52px; width: 53px; height: 53px; border-radius: 50%; background: var(--white); display: flex; align-items: center; justify-content: center; }
  .media.soap { top: 684px; background: linear-gradient(135deg, #3a2418 0%, #6a4a34 45%, #c9b99a 60%, #4a2e1e 100%); }
  .media.soap .caption { position: absolute; left: 108px; top: 108px; color: var(--white); font-family: "Inter", Arial, sans-serif; font-weight: 200; line-height: 1; }
  .media.soap .caption b { display: block; font-weight: 200; font-size: 25px; }
  .media.soap .caption span { display: block; font-size: 14px; margin: 1px 0 0 2px; }

  .content { position: absolute; left: 377px; top: 290px; width: 458px; }
  .content h1 { font-weight: 400; font-size: 31px; color: var(--orange); margin-bottom: 19px; }
  .content p { font-size: 13.4px; line-height: 21px; text-align: justify; margin-bottom: 21px; }

  .team-card { position: absolute; left: 881px; width: 270px; height: 286px; border: 1px solid var(--line); text-align: center; }
  .team-card.first { top: 295px; }
  .team-card.second { top: 590px; }
  .team-card .portrait { width: 170px; height: 170px; border-radius: 50%; margin: 28px auto 0; }
  .team-card.first .portrait { background: radial-gradient(circle at 50% 45%, #c9a48c 0%, #8a6552 45%, #d8d2cc 75%); }
  .team-card.second .portrait { background: radial-gradient(circle at 50% 45%, #c7a08a 0%, #5a4a40 45%, #cfcfcf 75%); }
  .team-card h4 { font-family: "Roboto", Arial, sans-serif; font-weight: 700; font-size: 16px; color: var(--ink); margin-top: 26px; }
  .team-card .role { font-family: "Roboto", Arial, sans-serif; font-size: 12px; color: #666; margin-top: 6px; }

  .footer { position: absolute; left: 0; top: 858px; width: 1200px; height: 42px; background: var(--footer); }
  .footer .copy { position: absolute; left: 52px; top: 18px; font-size: 11px; color: var(--orange); }
  .footer .social { position: absolute; right: 48px; top: 17px; display: flex; gap: 19px; }
  .footer .social span { width: 13px; height: 13px; border-radius: 50%; background: var(--orange-deep); }
</style>
</head>
<body>
  <header class="hero">
    <div class="hero-photo" role="img" aria-label="Photo of a woman in a white shirt holding a bar of soap on her open hand"></div>
    <div class="topbar">
      <div class="account">MY ACCOUNT<span>|</span>LOGIN</div>
      <div class="contact">HAVE A QUESTION? 1 800 7160<span>|</span><svg width="11" height="10" viewBox="0 0 11 10"><path d="M0 1h2l1.5 5h6L11 2.5H3" fill="none" stroke="#111" stroke-width="1.4"/><circle cx="4.5" cy="8.5" r="1" fill="#111"/><circle cx="8.5" cy="8.5" r="1" fill="#111"/></svg></div>
    </div>
    <div class="navband"></div>
    <nav class="nav">
      <a href="#">HOME</a>
      <a href="#" class="active">ABOUT US</a>
      <a href="#">OUR MISSION</a>
      <a href="#">SOAP PRODUCTS</a>
      <a href="#">FAQs</a>
      <a href="#">CONTACT US</a>
      <a href="#">BLOG</a>
      <a href="#" class="search"><svg width="13" height="13" viewBox="0 0 13 13"><circle cx="5.5" cy="5.5" r="4.2" fill="none" stroke="#111" stroke-width="2"/><path d="M8.6 8.6L12 12" stroke="#111" stroke-width="2.2"/></svg></a>
    </nav>
    <div class="brand"><span class="mark"></span><span class="name">PLUM</span></div>
    <div class="page-title">ABOUT US</div>
    <div class="back-home">Back to home <span class="arrow-box"><svg width="8" height="12" viewBox="0 0 8 12"><path d="M1.5 1l5 5-5 5" fill="none" stroke="#888" stroke-width="1.3"/></svg></span></div>
  </header>

  <aside class="categories">
    <h3>PRODUCT CATEGORIES</h3>
    <ul>
      <li>SUSPENDISSE</li>
      <li>FEUGIATMI</li>
      <li>SEDLECTUS</li>
      <li>MALESUADA</li>
      <li>PRUCA</li>
    </ul>
  </aside>

  <div class="media video" role="img" aria-label="Video still of smiling children gathered together outdoors">
    <span class="play"><svg width="12" height="16" viewBox="0 0 12 16"><path d="M2 1l9 7-9 7z" fill="#111"/></svg></span>
  </div>
  <div class="media soap" role="img" aria-label="Photo of natural soap bars with cinnamon sticks and star anise on wood">
    <div class="caption"><b>TUSPE</b><span>feugiat missee</span></div>
  </div>

  <main class="content">
    <h1>Aliquam amet ullamcor</h1>
    <p>gravida mollis. Tortor vitae tortor eros wisi facilisis. Consectetuer arcu ipsum ornare pellentesque, feugiat at. Aptent morbi nibh mauris a, tortor eu vel vel suscipit. Donec quam, erat ut vel cursus raesent integer leo orci aliquam, nibh a. Diam nobis eget, erat natoque integer fringilla viverra.</p>
    <p>Lorem ipsum dolor sit amet, ligula nulla pretium, rhoncus tempor placerat fermentum, enim integer ad vestibulum volutpat. isl turpis est, vel elit, congue wisi enim nunc ultricies sit, magna tincidunt. Maecenas aliquam maecenas ligula nostra, accumsan tacitic dolor ac adipiscing amet bibendum nullam, massa lacus molestie ut libero nec, diam et, pharetra sodales eget, feugiat</p>
  </main>

  <section class="team-card first">
    <div class="portrait" role="img" aria-label="Portrait of the senior manager"></div>
    <h4>MARA VELINSKA</h4>
    <div class="role">Senior Manager</div>
  </section>
  <section class="team-card second">
    <div class="portrait" role="img" aria-label="Portrait of the manager"></div>
    <h4>OWEN HALE</h4>
    <div class="role">Manager</div>
  </section>

  <footer class="footer">
    <div class="copy">© 2014 PLUM pure living under moonlight.&nbsp; All Rights Reserved.</div>
    <div class="social"><span></span><span></span><span></span><span></span></div>
  </footer>
</body>
</html>
```